Brain Risk Assessment

We need an illustration similar to the graphic attached that shows your brain performance lowers as you age. The goal of this is to show that if you make small changes earlier in life, it helps keep you sharp and prevents disease later on in life. If you change your brain health in your 40's and 50's, you made add 10 to 20 quality, brain healthy years to your life.

Target Market(s)

Consumer

Industry/Entity Type

Health

Font styles to use
Sans Serif

Colors
33a6d7
3276b5

Requirements
Must have
• Show multiple trajectories based on small improvements in brain health in 40's and 50's

```html
<!DOCTYPE html>
<html lang="en">
<head>
<meta charset="utf-8">
<title>Brain Risk Assessment</title>
<link rel="stylesheet" href="https://fonts.googleapis.com/css2?family=Cabin:ital,wght@0,400;0,700;1,700&family=Montserrat:wght@800&display=swap">
<style>
  :root {
    --title-red: #d9141b;
    --ink: #111111;
    --chart-blue: #4cc6ee;
    --curve-dark: #45bde8;
    --curve-light: #a9e1f5;
    --label-blue: #4dc3ea;
    --footer-band: #50cff3;
    --white: #ffffff;
  }
  html, body {
    margin: 0;
    padding: 0;
    width: 1139px;
    height: 1200px;
    overflow: hidden;
    background: var(--white);
  }
  .poster {
    display: block;
    width: 1139px;
    height: 1200px;
  }
  .title {
    font-family: "Montserrat", sans-serif;
    font-weight: 800;
    font-size: 62px;
    fill: var(--title-red);
  }
  .lead, .closing {
    font-family: "Cabin", sans-serif;
    font-size: 39px;
    fill: var(--ink);
  }
  .chart-label {
    font-family: "Cabin", sans-serif;
    font-weight: 700;
    font-size: 33px;
    fill: var(--label-blue);
  }
  .age-tick {
    font-family: "Cabin", sans-serif;
    font-size: 29px;
    fill: var(--chart-blue);
  }
  .axis, .tick, .boost-arrow {
    stroke: var(--chart-blue);
    stroke-width: 4;
    fill: none;
  }
  .boost-arrow { stroke-width: 2.5; }
  .trajectory-base { stroke: var(--curve-dark); stroke-width: 5; fill: none; }
  .trajectory-improved { stroke: var(--curve-light); stroke-width: 5; fill: none; }
  .arrow-head { fill: var(--chart-blue); }
  .footer-band { fill: var(--footer-band); }
  .footer-call {
    font-family: "Cabin", sans-serif;
    font-weight: 700;
    font-style: italic;
    font-size: 39px;
    fill: var(--white);
  }
  .footer-web {
    font-family: "Cabin", sans-serif;
    font-size: 37px;
    fill: var(--white);
  }
</style>
</head>
<body>
<svg class="poster" viewBox="0 0 1200 1264" xmlns="http://www.w3.org/2000/svg">
  <defs>
    <linearGradient id="brain-team-tones" x1="0" x2="1" y1="0" y2="0">
      <stop offset="0" stop-color="#d6eafa"/>
      <stop offset="0.5" stop-color="#c8f2d1"/>
      <stop offset="1" stop-color="#d6eafa"/>
    </linearGradient>
    <linearGradient id="life-stage-tones" x1="0" x2="1" y1="0" y2="0">
      <stop offset="0" stop-color="#e2f4fb"/>
      <stop offset="0.5" stop-color="#c6e9f7"/>
      <stop offset="1" stop-color="#eaf7fc"/>
    </linearGradient>
  </defs>

  <text class="title" x="193" y="93" textLength="858" lengthAdjust="spacingAndGlyphs">BRAIN RISK ASSESSMENT</text>
  <text class="lead" x="372" y="165" textLength="483" lengthAdjust="spacingAndGlyphs">Small changes earlier in life,</text>
  <text class="lead" x="90" y="218" textLength="1052" lengthAdjust="spacingAndGlyphs">it helps keep you sharp and prevents disease later on in life.</text>

  <rect class="brain-team-art" x="376" y="270" width="476" height="225" rx="60"
        fill="url(#brain-team-tones)" role="img"
        aria-label="Two brains with circular arrows around a group of cheering people of all ages"/>

  <g class="life-chart">
    <rect class="life-stages-art" x="235" y="778" width="725" height="126" rx="18"
          fill="url(#life-stage-tones)" role="img"
          aria-label="Silhouettes walking through life stages: crawling baby, toddler with ball, young adult, businessman, woman, elderly man with cane"/>

    <path class="trajectory-improved" d="M148 760 Q 585 470 1000 692"/>
    <path class="trajectory-base" d="M148 770 Q 565 540 997 765"/>

    <path class="boost-arrow" d="M518 656 V630"/>
    <path class="arrow-head" d="M512 632 L518 622 L524 632 Z"/>
    <path class="boost-arrow" d="M668 652 V615"/>
    <path class="arrow-head" d="M662 617 L668 607 L674 617 Z"/>
    <path class="boost-arrow" d="M865 692 V647"/>
    <path class="arrow-head" d="M859 649 L865 639 L871 649 Z"/>
    <path class="boost-arrow" d="M865 692 H972"/>
    <path class="arrow-head" d="M970 686 L982 692 L970 698 Z"/>

    <path class="axis" d="M148 920 V505"/>
    <path class="arrow-head" d="M137 507 L148 490 L159 507 Z"/>
    <path class="axis" d="M146 920 H1055"/>
    <path class="arrow-head" d="M1053 909 L1070 920 L1053 931 Z"/>

    <path class="tick" d="M525 910 V930 M640 910 V930 M838 910 V930 M1000 910 V930"/>
    <text class="age-tick" x="523" y="958" text-anchor="middle">25</text>
    <text class="age-tick" x="638" y="958" text-anchor="middle">50</text>
    <text class="age-tick" x="835" y="958" text-anchor="middle">75</text>
    <text class="age-tick" x="1000" y="958" text-anchor="middle">100</text>

    <text class="chart-label" x="188" y="552" textLength="140" lengthAdjust="spacingAndGlyphs">Improve</text>
    <text class="chart-label" x="188" y="596" textLength="215" lengthAdjust="spacingAndGlyphs">performance</text>
    <text class="chart-label" x="928" y="560" textLength="94" lengthAdjust="spacingAndGlyphs">Delay</text>
    <text class="chart-label" x="928" y="604" textLength="118" lengthAdjust="spacingAndGlyphs">disease</text>
  </g>

  <text class="closing" x="140" y="1030" textLength="935" lengthAdjust="spacingAndGlyphs">If you change your brain health in your 40's and 50's,</text>
  <text class="closing" x="52" y="1083" textLength="1113" lengthAdjust="spacingAndGlyphs">you made add 10 to 20 quality, brain healthy years to your life.</text>

  <rect class="footer-band" x="0" y="1130" width="1200" height="134"/>
  <text class="footer-call" x="207" y="1196" textLength="756" lengthAdjust="spacingAndGlyphs">For more info Call Us Now 0000000000</text>
  <text class="footer-web" x="399" y="1244" textLength="407" lengthAdjust="spacingAndGlyphs">www.yourwebsite.com</text>
</svg>
</body>
</html>
```